Vorlage für ein Workbook
Zielgruppe
Coaching und Beratung
Aufgabenstellung
Es soll eine Vorlage für ein Workbook erstellt werden, das ich dann selbst mit Inhalten füllen kann.. evtl. mit Canvas oder wie auch immer....
Es ist ein 12 Wochenkurs, d.h. ich brauche 1 Titelseite für jede Woche, die ich dann paste und copy machen kann und beschriften kann, sowie eine Vorlage für die einzelnen Seiten des Workbooks. Das Workbook in pdf Format muss auch online ausgefüllt werden können.
Design angepasst an Landingpage

```html
<!DOCTYPE html>
<html lang="en">
<head>
<meta charset="utf-8">
<title>Workbook Cover Templates</title>
<link rel="stylesheet" href="https://fonts.googleapis.com/css2?family=Cinzel:wght@400&display=swap">
<style>
  :root {
    --page-bg: #ffffff;
    --sheet: #c4bdb5;
    --sage: #b3bca6;
    --mist: #c9d0d8;
    --line: #f6ede7;
    --ink-light: #f7f1ec;
    --ink-navy: #7a8294;
    --leaf-light: #d9d0ca;
  }
  * { margin: 0; padding: 0; box-sizing: border-box; }
  html, body {
    width: 865px;
    height: 1200px;
    overflow: hidden;
    background: var(--page-bg);
  }
  .sheet-grid { position: relative; width: 865px; height: 1200px; }
  .cover {
    position: absolute;
    width: 396px;
    height: 560px;
    background: var(--sheet);
    overflow: hidden;
  }
  .cover--one   { left: 24px;  top: 27px; }
  .cover--two   { left: 443px; top: 27px; }
  .cover--three { left: 24px;  top: 609px; }
  .cover--four  { left: 443px; top: 609px; }
  .cover-art { position: absolute; inset: 0; width: 100%; height: 100%; }
  .blob--sage { fill: var(--sage); }
  .blob--mist { fill: var(--mist); }
  .flow-line { fill: none; stroke: var(--line); stroke-width: 2; }
  .leaf-area--light { fill: var(--leaf-light); opacity: 0.5; }
  .leaf-area--navy { fill: var(--ink-navy); opacity: 0.3; }
  .cover-text {
    position: absolute;
    left: 68px;
    top: 197px;
    width: 310px;
    color: var(--ink-light);
    font-family: "Cinzel", "Times New Roman", serif;
    text-transform: uppercase;
  }
  .cover-title {
    font-size: 33px;
    font-weight: 400;
    letter-spacing: 0.3px;
    line-height: 1;
    white-space: nowrap;
  }
  .cover-lead {
    margin-top: 15px;
    font-size: 7px;
    line-height: 10px;
    letter-spacing: 0;
    white-space: nowrap;
  }
</style>
</head>
<body>
<main class="sheet-grid">

  <section class="cover cover--one">
    <svg class="cover-art" viewBox="0 0 595 842" preserveAspectRatio="none">
      <path class="blob--sage" d="M0 0 H215 C230 60 235 150 200 155 C160 160 120 110 90 130 C70 150 70 175 40 165 C20 160 0 140 0 130 Z"/>
      <path class="flow-line" d="M245 0 C255 100 235 165 150 180 C110 188 100 210 70 250 C55 265 20 265 0 262"/>
      <path class="blob--sage" d="M595 460 C540 455 500 480 480 540 C460 565 420 560 380 580 C340 610 335 660 320 720 C300 770 270 760 220 765 C170 770 140 810 140 842 H595 Z"/>
      <path class="flow-line" d="M595 425 C520 450 470 520 475 640 C480 740 470 790 400 790 C320 790 230 800 200 842"/>
      <rect class="leaf-area--light" x="380" y="0" width="215" height="185" rx="40" role="img" aria-label="Line-drawn leafy branch with berries"/>
      <rect class="leaf-area--light" x="0" y="550" width="145" height="292" rx="40" role="img" aria-label="Line-drawn leafy branch with berries"/>
    </svg>
    <div class="cover-text">
      <h1 class="cover-title">Lorem Ipsum</h1>
      <p class="cover-lead">Lorem ipsum dolor sit amet, consectetuer adipiscing elit,<br>sed diam nonummy nibh euismod tincidunt ut laoreet<br>dolore magna aliquam</p>
    </div>
  </section>

  <section class="cover cover--two">
    <svg class="cover-art" viewBox="0 0 595 842" preserveAspectRatio="none">
      <path class="flow-line" d="M0 60 C60 40 110 40 160 60 C200 75 220 110 260 110 C310 110 320 40 350 0"/>
      <path class="flow-line" d="M0 110 C100 60 160 100 220 150 C260 180 290 185 330 165 C390 130 420 20 530 0"/>
      <path class="blob--mist" d="M0 568 C70 565 115 600 130 660 C145 730 160 790 230 815 C260 830 280 842 290 842 H0 Z"/>
      <rect class="leaf-area--light" x="305" y="505" width="290" height="337" rx="60" role="img" aria-label="Line-drawn leafy branch with berries"/>
    </svg>
    <div class="cover-text">
      <h1 class="cover-title">Lorem Ipsum</h1>
      <p class="cover-lead">Lorem ipsum dolor sit amet, consectetuer adipiscing elit,<br>sed diam nonummy nibh euismod tincidunt ut laoreet<br>dolore magna aliquam</p>
    </div>
  </section>

  <section class="cover cover--three">
    <svg class="cover-art" viewBox="0 0 595 842" preserveAspectRatio="none">
      <rect class="leaf-area--navy" x="0" y="0" width="505" height="250" rx="50" role="img" aria-label="Hand-drawn navy branch with leaves and berries"/>
      <path class="flow-line" d="M0 350 C40 450 120 480 230 480 C330 480 345 520 345 600 C345 720 370 800 460 842"/>
      <path class="flow-line" d="M0 515 C80 515 200 520 230 560 C250 600 200 660 215 720 C230 780 270 820 300 842"/>
      <path class="flow-line" d="M0 575 C70 570 170 565 195 590 C220 620 140 700 155 750 C170 790 195 810 185 842"/>
      <path class="blob--mist" d="M250 842 C255 800 300 790 360 790 C400 780 395 720 405 680 C420 620 470 600 500 580 C530 560 560 545 595 550 V842 Z"/>
    </svg>
    <div class="cover-text">
      <h1 class="cover-title">Lorem Ipsum</h1>
      <p class="cover-lead">Lorem ipsum dolor sit amet, consectetuer adipiscing elit,<br>sed diam nonummy nibh euismod tincidunt ut laoreet<br>dolore magna aliquam</p>
    </div>
  </section>

  <section class="cover cover--four">
    <svg class="cover-art" viewBox="0 0 595 842" preserveAspectRatio="none">
      <path class="blob--sage" d="M215 0 C220 50 250 100 290 120 C330 135 320 190 340 230 C380 290 450 280 500 300 C540 320 520 420 530 430 C540 450 580 455 595 455 V0 Z"/>
      <path class="flow-line" d="M215 0 C260 90 330 120 430 120 C530 120 580 150 585 240 C590 300 585 330 595 345"/>
      <path class="blob--mist" d="M0 570 C60 565 110 560 130 620 C150 680 145 740 170 790 C180 800 150 810 0 830 Z"/>
      <path class="blob--sage" d="M0 842 C20 810 80 800 140 805 C200 805 230 740 300 700 C340 680 400 700 450 670 C500 640 540 640 595 640 V842 Z"/>
      <rect class="leaf-area--navy" x="40" y="430" width="240" height="412" rx="60" role="img" aria-label="Hand-drawn navy leafy stem"/>
    </svg>
    <div class="cover-text">
      <h1 class="cover-title">Lorem Ipsum</h1>
      <p class="cover-lead">Lorem ipsum dolor sit amet, consectetuer adipiscing elit,<br>sed diam nonummy nibh euismod tincidunt ut laoreet<br>dolore magna aliquam</p>
    </div>
  </section>

</main>
</body>
</html>
```